Cool cafe needs help with our corporate identity.

We have a logo! We have a font!

What we need is to tie it together for
1. A menu
2. Labels for jam and other things we sell
3. Business Cards

All should have the same design style.

We have a strong design aesthetic in the cafe. Lots of colour and quirky objects. See this Snapvue profile for photos (you can download high-res from here if you sign into Snapvue): http://www.snapvue-example.com/photos/58216407@K31/

Also our website is www.maudwalrus.example

A main feature is the counter that is made of yardsticks.

There is also a bit of and 80's feel. Especially images of Edmund and Fen (the Royals).

We also like weird taxidermy and anthropology images from the 1920s. Gerald P. Stanwick was an anthropologist who used to own a Walrus called Maud. That is where our name comes from. Google 'Gerald P. Stanwick' for interesting images.

Perhaps design elements could be taken from any of these themes, although we are open to other ideas.

We like being playful and irreverent.

The logo is the words Maud Walrus in Cursive. We want to stick with that. The font we like is Tallow Works Brisk. The logo is currently blue colour - this can change.

1.Menu Specs
We like printing this ourselves. Thick paper A4 with a fold seems to work well. We want some design elements added. Our existing menu is attached.

2. Labels
We have jam jars and labels for biscuits. These are various sizes. It needs to have the name of the jam,e.g. Apricot, The Maud Walrus Logo, Some design elements, A list of ingredients, and the weight. Eg 250g.

3. Business Card
A standard sized business card with The logo, design elements and the following words:
Maud Walrus Cafe
17 Kelvane Street, Ardley North
03 9017 4426
www.maudwalrus.example

Target Market(s)

Adults based in Melbourne, Australia that like design and are kind of hipsterish,

Industry/Entity Type

Printing

Requirements
Must have
• Logo and font as described.
Nice to have
• Maybe a bit quirky.
Should not have
• Slick corporate look.

```html
<!DOCTYPE html>
<html lang="en">
<head>
<meta charset="utf-8">
<title>Maud Walrus Cafe – Business Card</title>
<link rel="stylesheet" href="https://fonts.googleapis.com/css2?family=Bitter:wght@800&display=swap">
<style>
  :root {
    --page: #e9e9e9;
    --navy: #2a2670;
    --paper: #faf8f4;
    --paper-tone: #ddd5c7;
    --paper-mid: #ebe5db;
    --ink: #1e1c1a;
    --white: #ffffff;
    --text-font: "Bitter", Georgia, serif;
  }
  * { box-sizing: border-box; margin: 0; padding: 0; }
  html, body {
    width: 1200px;
    height: 1000px;
    overflow: hidden;
    background: var(--page);
  }
  .sheet {
    position: relative;
    width: 1200px;
    height: 1000px;
  }
  .card {
    position: absolute;
    left: 238px;
    width: 724px;
    height: 362px;
    border-radius: 22px;
    overflow: hidden;
  }
  .card--back {
    top: 100px;
    background: var(--navy);
  }
  .card--front {
    top: 532px;
    background: var(--paper);
  }
  .card__texture {
    position: absolute;
    inset: 0;
    background:
      radial-gradient(ellipse 120px 60px at 12% 20%, var(--paper-tone), transparent 70%),
      radial-gradient(ellipse 160px 70px at 85% 15%, var(--paper-tone), transparent 70%),
      radial-gradient(ellipse 200px 80px at 70% 85%, var(--paper-tone), transparent 70%),
      radial-gradient(ellipse 150px 70px at 20% 88%, var(--paper-tone), transparent 70%),
      radial-gradient(ellipse 140px 60px at 95% 55%, var(--paper-tone), transparent 70%),
      radial-gradient(ellipse at 48% 35%, var(--paper) 0%, var(--paper) 30%, var(--paper-mid) 75%, var(--paper-tone) 100%);
  }
  .logo-lockup {
    position: absolute;
    display: flex;
    align-items: flex-start;
    gap: 14px;
    white-space: nowrap;
  }
  .wordmark {
    font-family: var(--text-font);
    font-weight: 800;
    line-height: 1;
  }
  .card--back .logo-lockup {
    left: 150px;
    top: 150px;
  }
  .card--back .wordmark {
    font-size: 66px;
    color: var(--white);
  }
  .wordmark-suffix {
    font-family: var(--text-font);
    font-weight: 800;
    font-size: 19px;
    color: var(--white);
    padding-top: 4px;
  }
  .card--front .logo-lockup {
    left: 22px;
    top: 142px;
  }
  .card--front .wordmark {
    font-size: 38px;
    color: var(--navy);
  }
  .contact {
    position: absolute;
    left: 306px;
    top: 50px;
    font-family: var(--text-font);
    font-weight: 800;
    font-style: normal;
    color: var(--ink);
    font-size: 17px;
    line-height: 29px;
  }
  .contact__name {
    color: var(--navy);
    font-size: 21px;
    line-height: 36px;
  }
</style>
</head>
<body>
  <main class="sheet">
    <section class="card card--back" aria-label="Business card, back">
      <div class="logo-lockup">
        <span class="wordmark">Maud Walrus</span>
        <span class="wordmark-suffix">Cafe</span>
      </div>
    </section>

    <section class="card card--front" aria-label="Business card, front">
      <div class="card__texture" role="img" aria-label="Distressed beige scratch texture across the card"></div>
      <div class="logo-lockup">
        <span class="wordmark">Maud Walrus</span>
      </div>
      <address class="contact" style="top:52px;">
        <div class="contact__name">Maud Walrus Café</div>
        <div>17 Kelvane Street, Ardley North 3071</div>
        <div>(03) 9017 4426</div>
        <div>www.maudwalrus.example</div>
      </address>
    </section>
  </main>
</body>
</html>
```